One pager fact sheet for healthcare companies

We are looking for a designer to create a theme based off this example. The project will consist of building a layout and theme for a one page, front and back handout. The handout will be used as part of an educational series for medical professionals. The format must be suitable for print production. The theme should be clear, concise, and professional. Cluttered graphics will not be useable.
This project has potential to include additional work over the next 3 months.

Target Market(s)

Healthcare professionals

Industry/Entity Type

Healthcare

Font styles to use
Serif
Sans Serif

Requirements
Must have
• A professional look and feel
Should not have
• Cluttered graphics or busy look

```html
<!DOCTYPE html>
<html lang="en">
<head>
<meta charset="utf-8">
<title>Health System Fact Sheet</title>
<link href="https://fonts.googleapis.com/css2?family=Open+Sans:wght@300;400;600;700&family=Oswald:wght@400&display=swap" rel="stylesheet">
<style>
:root{
  --blue:#1565b0;
  --blue-dark:#0f4f91;
  --sky:#dcedfa;
  --sky-soft:#eaf4fc;
  --ink:#7a7a7a;
  --ink-dark:#333;
  --paper:#ffffff;
  --bg:#d6d6d6;
}
*{box-sizing:border-box;margin:0;padding:0}
html,body{width:1200px;height:1200px;overflow:hidden}
body{background:var(--bg);font-family:"Open Sans",Arial,sans-serif;position:relative}
.page{position:absolute;top:236px;width:640px;height:904px;background:var(--paper);transform:scale(.8);transform-origin:0 0;overflow:hidden;box-shadow:0 6px 18px rgba(0,0,0,.25)}
.page.front{left:61px}
.page.back{left:616px}
.abs{position:absolute}
.logo{color:#fff;font-weight:400;letter-spacing:.3px}
.sec-head{position:absolute;height:42px}
.sec-icon{position:absolute;left:0;top:0;width:48px;height:42px;background:var(--sky);display:flex;align-items:center;justify-content:center}
.sec-bar{position:absolute;left:50px;top:13px;height:25px;background:var(--blue);color:#fff;font-family:"Oswald",Arial,sans-serif;font-size:16.5px;line-height:25px;padding-left:10px;white-space:nowrap;clip-path:polygon(0 0,100% 0,calc(100% - 4px) 100%,0 100%)}
.sec-bar.tall{height:46px;line-height:20px;padding-top:3px;top:0}
.col{position:absolute}
.col h3{color:var(--blue);font-weight:400;font-size:12.5px;margin:7px 0 2px;white-space:nowrap}
.col p,.col li{color:var(--ink);font-size:8.5px;line-height:14px}
.col ul{list-style:none}
.col li{position:relative;padding-left:9px}
.col li::before{content:"";position:absolute;left:0;top:5.5px;width:3.5px;height:3.5px;border-radius:50%;background:var(--blue)}
.col li b{color:#444;font-weight:700}
.col p+p{margin-top:3px}
.col.compact li{font-size:8.2px;line-height:13px}
.col.compact li::before{top:5px}
.col.tight h3{letter-spacing:-.35px}
.checks{color:var(--ink);font-size:8.5px;line-height:15px}
.checks span{display:inline-block;margin-right:10px}
.checks i{display:inline-block;width:24px;border-bottom:1px solid #999;text-align:center;font-style:normal;font-size:7.5px;line-height:10px;margin-right:2px;color:#333}
.contact{position:absolute;left:488px;top:22px}
.contact div{display:flex;align-items:center;gap:10px;color:var(--blue);font-size:10px;font-weight:600;height:19.5px}
.footer-url{position:absolute;color:#fff;font-size:12px;letter-spacing:1.2px}
.ph{position:absolute}
</style>
</head>
<body>

<section class="page front">
  <svg class="abs" style="left:0;top:0" width="640" height="100" viewBox="0 0 640 100">
    <defs>
      <linearGradient id="hdrPhoto" x1="0" x2="1" y1="0" y2="0">
        <stop offset="0" stop-color="#2b6fb7"/>
        <stop offset="1" stop-color="#e8eef6"/>
      </linearGradient>
    </defs>
    <rect width="640" height="97" fill="#1565b0"/>
    <polygon points="272,0 425,0 462,97 272,97" fill="url(#hdrPhoto)"/>
    <polygon points="425,0 640,0 640,97 462,97" fill="#dcedfa"/>
    <rect y="96" width="640" height="3" fill="#cfe6f8"/>
  </svg>
  <div class="ph" style="left:272px;top:0;width:190px;height:97px" role="img" aria-label="Photo of a physician holding a stethoscope and clipboard"></div>
  <div class="logo abs" style="left:22px;top:25px;font-size:32px">Company Logo</div>
  <div class="contact">
    <div><svg width="14" height="14" viewBox="0 0 14 14"><circle cx="7" cy="4" r="3" fill="#1565b0"/><path d="M1 13c0-4 3-5 6-5s6 1 6 5z" fill="#1565b0"/></svg>Name</div>
    <div><svg width="14" height="14" viewBox="0 0 14 14"><path d="M7 13S2.5 7.8 2.5 5a4.5 4.5 0 0 1 9 0C11.5 7.8 7 13 7 13z" fill="#1565b0"/><circle cx="7" cy="5" r="1.7" fill="#dcedfa"/></svg>Address</div>
    <div><svg width="14" height="14" viewBox="0 0 14 14" fill="none" stroke="#1565b0" stroke-width="1.2"><circle cx="7" cy="7" r="5.6"/><ellipse cx="7" cy="7" rx="2.4" ry="5.6"/><path d="M1.4 7h11.2M2.3 4h9.4M2.3 10h9.4"/></svg>www.company.com</div>
  </div>

  <div class="sec-head" style="left:20px;top:112px;width:210px">
    <span class="sec-icon"><svg width="22" height="22" viewBox="0 0 22 22"><circle cx="8" cy="8" r="5.5" fill="none" stroke="#111" stroke-width="3"/><path d="M12 12l7 7" stroke="#111" stroke-width="4" stroke-linecap="round"/></svg></span>
    <span class="sec-bar" style="width:130px">KEY FACTS</span>
  </div>
  <div class="col" style="left:20px;top:156px;width:290px">
    <h3>Organization Type:</h3>
    <p>Not for Profit Health System</p>
    <h3 style="margin-top:10px">Leadership Team and Contact Information:</h3>
    <ul>
      <li>Laura K. Benton, CEO</li>
      <li>Marcus T. Hale, II, President</li>
      <li>Daniel P. Crowe, EVP and COO14</li>
      <li>Steven Ardell, Jr. MD, EVP and Chief Medical Officer</li>
    </ul>
    <h3 style="margin-top:7px">Physicians in Network:</h3>
    <ul>
      <li><b>Total:</b> 2,400 Salaried, 3,000 Affiliated</li>
      <li><b>PCPs:</b> 1,000 Salaried, 1,500 Affiliated</li>
      <li><b>Ophthalmologists:</b> 35 Salaried, 0 Affiliated</li>
      <li><b>Retina Specialists:</b> 10 Salaried, 0 Affiliated</li>
    </ul>
    <h3 style="margin-top:7px">Covered Lives:</h3>
    <p>800,000</p>
  </div>

  <div class="sec-head" style="left:20px;top:413px;width:210px">
    <span class="sec-icon"><svg width="24" height="24" viewBox="0 0 24 24" fill="none" stroke="#111" stroke-width="2"><circle cx="9" cy="9" r="4"/><path d="M9 2v3M9 13v3M2 9h3M13 9h3M4 4l2 2M12 12l2 2M4 14l2-2M12 6l2-2"/><circle cx="18" cy="18" r="2.5"/><path d="M18 13.5v2M18 20.5v2M13.5 18h2M20.5 18h2"/></svg></span>
    <span class="sec-bar" style="width:130px">SERVICES</span>
  </div>
  <div class="col" style="left:20px;top:459px;width:290px">
    <h3>Key Services and Facilities</h3>
    <ul>
      <li>Major service lines: cardiac care, women's and children's services, cancer care, orthopedics, transplants, neuroscience, trauma, and urology</li>
      <li>Key Facilities: ClearView Eye centers include offices for ophthalmologists and retina specialists</li>
    </ul>
    <h3 style="margin-top:8px">Distribution of Outpatient Services</h3>
    <ul>
      <li><b>In Facilities:</b> 40%</li>
      <li><b>In Owned Practices:</b> 30%</li>
      <li><b>In Affiliated Practices:</b> 20%</li>
      <li><b>Unaffiliated/ Out of Network:</b> 10%</li>
    </ul>
  </div>
  <div class="ph" style="left:30px;top:640px;width:300px;height:220px;background:radial-gradient(ellipse at 50% 60%,#e6eef6 0%,#f6f9fc 70%,#fff 100%)" role="img" aria-label="Photo of a team of smiling doctors and nurses in white coats and scrubs"></div>

  <div class="sec-head" style="left:343px;top:112px;width:240px">
    <span class="sec-icon"><svg width="22" height="22" viewBox="0 0 22 22" fill="#111"><rect x="2" y="2" width="18" height="5" rx="1"/><rect x="2" y="9" width="18" height="5" rx="1"/><rect x="2" y="16" width="18" height="5" rx="1"/><g fill="#dcedfa"><circle cx="16" cy="4.5" r="1"/><circle cx="16" cy="11.5" r="1"/><circle cx="16" cy="18.5" r="1"/></g></svg></span>
    <span class="sec-bar" style="width:183px">SYSTEM STRUCTURE</span>
  </div>
  <div class="col" style="left:343px;top:158px;width:275px">
    <h3>Geographic Coverage:</h3>
    <p>Michigan</p>
    <h3 style="margin-top:10px">Number of Hospitals and Facilities:</h3>
    <ul>
      <li>7 Hospitals</li>
      <li>Over 35 medical centers and facilities across multiple counties in Michigan</li>
    </ul>
    <h3 style="margin-top:8px">Key Affiliations:</h3>
    <ul>
      <li>Medical Group has more than 1,100 physicians that staff Fairhaven hospital, Westmere hospital, and 26 medical centers</li>
      <li>Physician Network is a physician-led subsidiary, comprising the Medical Group, hospital-employed and private practice physicians</li>
      <li>2,000 affiliated private practice physicians</li>
    </ul>
  </div>

  <div class="sec-head" style="left:343px;top:388px;width:270px;height:48px">
    <span class="sec-icon" style="height:62px;top:-1px"><svg width="26" height="26" viewBox="0 0 26 26" fill="none" stroke="#111" stroke-width="2"><circle cx="9" cy="13" r="5"/><path d="M9 18v6M6 21h6"/><circle cx="16" cy="10" r="5"/><path d="M19.5 6.5L24 2M20 2h4v4"/></svg></span>
    <span class="sec-bar tall" style="width:218px">KEY PAYER RELATIONSHIPS AND<br>PAYMENT MODELS</span>
  </div>
  <div class="col compact" style="left:343px;top:455px;width:285px">
    <h3>Key Plans:</h3>
    <ul>
      <li>Northfield Health</li>
      <li>Lakeshore Shield</li>
      <li>Harborcare Network</li>
      <li>Veridia</li>
      <li>Westbrook</li>
      <li>Medicare</li>
      <li>Michigan Medicaid</li>
      <li>Corvane</li>
      <li>Keystone Health</li>
      <li>Unity Plans</li>
    </ul>
    <h3 style="margin-top:8px">Level of Risk Taken</h3>
    <ul>
      <li>80% of revenue is billed under a risk-based payment scheme</li>
      <li>Half of these lives include the risk for outpatient, physician-administered biologics</li>
    </ul>
    <ul style="margin-top:7px">
      <li>COMPANY accepts a variety of risk-based payment models including full and partial risk, bundled payments, and ACO contracts.</li>
      <li>All decisions to join an ACO or participate in a risk-based contract are made at the corporate level.</li>
      <li>COMPANY is contracted with CMS as a Next Generation ACO. Through the HMO product, this contract represents 30% of the health system's revenue and covers over 20,000 Medicare lives.</li>
      <li>The remaining share of revenue typically includes a value-based payment model. Contracts with private payers, such as Lakeshore Shield, incorporate contracts based on performance and quality of care which may lead to bonus payments.</li>
    </ul>
  </div>

  <svg class="abs" style="left:0;top:860px" width="640" height="44" viewBox="0 0 640 44">
    <rect width="640" height="44" fill="#dcedfa"/>
    <polygon points="0,0 190,0 212,44 0,44" fill="#1565b0"/>
  </svg>
  <div class="footer-url" style="left:35px;top:874px">www.company.com</div>
</section>

<section class="page back">
  <div class="ph" style="left:0;top:0;width:640px;height:286px;background:linear-gradient(180deg,#eef4f9 0%,#d9e6f1 70%,#b9cfe6 100%)" role="img" aria-label="Photo of a stethoscope and blood pressure gauge on a light blue surface"></div>
  <svg class="abs" style="left:0;top:0" width="640" height="286" viewBox="0 0 640 286">
    <polygon points="0,0 270,0 328,115 60,115 0,30" fill="#1565b0"/>
    <polygon points="0,30 60,115 0,115" fill="#dcedfa"/>
    <rect y="255" width="640" height="31" fill="#cfe0f1" opacity=".7"/>
  </svg>
  <div class="logo abs" style="left:63px;top:37px;font-size:30px;font-weight:300">Company Logo</div>

  <div class="sec-head" style="left:28px;top:311px;width:300px">
    <span class="sec-icon"><svg width="24" height="16" viewBox="0 0 24 16"><path d="M1 8C5 1 19 1 23 8C19 15 5 15 1 8z" fill="#111"/><circle cx="12" cy="8" r="4" fill="#dcedfa"/><circle cx="12" cy="8" r="2.2" fill="#111"/></svg></span>
    <span class="sec-bar" style="width:244px">RETINA SPECIALIST &nbsp;REIMBURSEMENT</span>
  </div>
  <div class="col" style="left:28px;top:357px;width:295px">
    <h3>Dominant Reimbursement Models Used:</h3>
    <div class="checks">
      <span><i></i>Fee for Service (FFS)</span><span><i></i>Reduced FFS w/ withholding</span><br>
      <span><i></i>FFS with bonus</span><span><i>x</i>Salaried plus bonus</span><span><i></i>Capitation</span>
    </div>
    <h3>Incentive Programs:</h3>
    <div class="checks"><span><i>x</i>Bonus Pools</span><span><i></i>Shared Savings</span></div>
    <p style="margin-top:8px">Salaried retina specialists are eligible for bonus payments based on key performance metrics.</p>
    <p>Through Meridian, the integrated electronic health record platform, data is collected on productivity metrics such as number of patients treated, drug costs, and quality of care. Quality metrics are specific to eye care as well as related to general patient care.</p>
    <p>Calculations for bonus payments are measured across the entire medical group and not individually by specialty. Exclusions may be made for outlier patient cases.</p>
  </div>

  <div class="sec-head" style="left:28px;top:617px;width:300px">
    <span class="sec-icon"><svg width="22" height="22" viewBox="0 0 22 22" fill="#111"><circle cx="11" cy="4" r="2.5"/><rect x="9" y="7" width="4" height="5"/><path d="M4 12h14v2h-1v-1H5v1H4z"/><circle cx="4" cy="16" r="2"/><circle cx="11" cy="16" r="2"/><circle cx="18" cy="16" r="2"/><rect x="2.5" y="18" width="3" height="3"/><rect x="9.5" y="18" width="3" height="3"/><rect x="16.5" y="18" width="3" height="3"/></svg></span>
    <span class="sec-bar" style="width:200px">RETINA SPECIALIST REFERRALS</span>
  </div>
  <div class="col" style="left:28px;top:664px;width:260px">
    <h3>Retina specialist network development</h3>
    <p>Health System is not pursuing acquisitions of retina specialist practices currently. The presence of academic institutions and teaching facilities ensures there is no shortage of retina specialists in the southern eastern portion of Michigan.</p>
    <h3 style="margin-top:9px">Referral Process</h3>
    <p>Health System leverages the EHR capabilities to facilitate in-network referrals. Primary care physicians can refer patients directly to retina specialist offices during the patient's visit. Referrals among physicians are based on physician relationships, not directed to specific providers by the health system.</p>
  </div>

  <div class="sec-head" style="left:352px;top:311px;width:240px">
    <span class="sec-icon"><svg width="20" height="22" viewBox="0 0 20 22" fill="none" stroke="#111" stroke-width="1.8"><circle cx="10" cy="13" r="7.5"/><path d="M10 13V8M8 2h4M10 2v3.5M16 5l1.5-1.5"/></svg></span>
    <span class="sec-bar" style="width:178px">ANTI-VEGF MANAGEMENT</span>
  </div>
  <div class="col tight" style="left:352px;top:357px;width:276px">
    <h3>Process Exists for Anti-VEGF Drug Management?</h3>
    <div class="checks"><span><i>x</i>Yes, for salaried physicians</span><span><i></i>Yes, for affiliated physicians</span><span><i></i>No</span></div>
    <h3>Use of EHR system and Anti-VEGF Drugs</h3>
    <div class="checks"><span><i>x</i>Yes, for monitoring Rx</span><span><i></i>Yes, for influencing Rx</span><br><span><i></i>No</span></div>
    <h3>Anti-VEGF Management Tools Utilized</h3>
    <div class="checks">
      <span><i>x</i>Prescriber Education</span><span><i></i>CPOE</span><span><i></i>Centralized Formulary</span>
      <span><i></i>Preferred Product Lists</span><span><i></i>Centralized Drug Supply</span>
      <span><i></i>Prior Authorizations</span><span><i></i>Step Therapy</span>
      <span><i></i>Treatment Pathways</span><span><i></i>Utilization Reports</span>
      <span><i></i>Consensus Building</span><span><i></i>Newsletters</span><span><i></i>Outlier Counseling</span>
    </div>
    <p style="margin-top:22px">Health System does not direct physician prescribing of anti-VEGF medications.</p>
    <p>HMO currently has a formulary with Ocuvance and Retinova preferred. Due to the Next Generation ACO contract adopting the HMO management policies, all ACO patients are subject to the health plan's management. This includes prior authorizations, preferred products, and step therapy. HMO and ACO patients are required to try and fail either Ocuvance or Retinova before approval of Visterra is attained.</p>
    <p>Patients covered under other payers must follow the criteria set forth by the patient's health plan. If there is no preferred product or management tool indicated in the medical policy, retina specialists may prescribe their drug of choice without restriction from the health system.</p>
  </div>

  <svg class="abs" style="left:0;top:860px" width="640" height="44" viewBox="0 0 640 44">
    <rect width="640" height="44" fill="#dcedfa"/>
    <polygon points="446,0 640,0 640,44 426,44" fill="#1565b0"/>
  </svg>
  <div class="footer-url" style="left:471px;top:874px">www.company.com</div>
</section>

</body>
</html>
```